Web Design For Manufacturing And Outsourcing Company

Pick up the pieces from our previous developer and help us complete our website.

5 pages - Home,Machining,Sourcing,About Us, and Contact

Attached you will find screen shots of previous direction but we're open to new ideas.

We can provide all text and images needed.

Thanks!

5+ page

```html
<!DOCTYPE html>
<html lang="en">
<head>
<meta charset="utf-8">
<title>Kestrel Works — Machining &amp; Sourcing</title>
<link href="https://fonts.googleapis.com/css2?family=Open+Sans:wght@400;600&family=PT+Sans:wght@400;700&display=swap" rel="stylesheet">
<style>
:root{
  --orange:#ee5020;
  --ink:#1c1c1c;
  --dark:#222222;
  --panel:#2d2d2d;
  --grey:#b9b9b9;
  --muted:#9a9a9a;
  --text:#333333;
  --white:#ffffff;
}
*{box-sizing:border-box;margin:0;padding:0}
html,body{width:1200px;height:2830px;overflow:hidden;background:var(--white)}
body{position:relative;font-family:"Open Sans",Arial,sans-serif;color:var(--text)}
.abs{position:absolute}
.heading{font-family:"PT Sans",Arial,sans-serif;font-weight:700}

/* header */
.site-header{left:0;top:0;width:1200px;height:57px;background:var(--dark)}
.brand{left:145px;top:15px;display:flex;align-items:center;gap:8px;font-family:"PT Sans",Arial,sans-serif;font-weight:700;font-size:18px;letter-spacing:2px;color:var(--orange)}
.brand-mark{width:18px;height:18px;background:var(--white)}
.main-nav{right:145px;top:20px;display:flex;gap:37px;font-size:12px}
.main-nav a{color:var(--white);text-decoration:none}
.main-nav a.active{color:var(--orange)}

/* hero */
.hero-photo{left:0;top:57px;width:1200px;height:594px;background:linear-gradient(120deg,#b9c6d3 0%,#dfe6ee 40%,#9eb4c8 70%,#4e5e6f 100%)}
.hero-caption{left:387px;top:270px;width:428px;height:83px;background:rgba(34,34,34,.88);color:var(--white);font-size:23px;line-height:32px;text-align:center;padding-top:10px}
.slide-arrow{top:296px}
.btn{display:block;text-align:center;font-size:13px;text-decoration:none;color:var(--white)}
.btn-orange{background:var(--orange)}
.btn-dark{background:var(--panel);position:absolute}
.btn-dark::after{content:"";position:absolute;left:0;bottom:0;width:60%;height:7px;background:var(--orange);clip-path:polygon(0 0,100% 100%,0 100%)}

/* about */
.about-title{left:145px;top:722px;font-size:35px;color:var(--orange)}
.about-sub{left:145px;top:780px;font-family:"PT Sans",Arial,sans-serif;font-size:25px;color:var(--ink)}
.about-copy{left:145px;top:826px;width:520px;font-size:16.5px;line-height:28.5px;color:var(--text)}
.about-photo{left:715px;top:732px;width:340px;height:340px;background:linear-gradient(135deg,#4a4a4a 0%,#5fb6c5 35%,#7fd3dd 60%,#d8d8d8 100%)}

/* services */
.service-icon{width:82px;height:80px;left:559px;border-radius:10px}
.service-title{left:0;width:1200px;text-align:center;font-size:31px;color:var(--white)}
.service-copy{left:170px;width:860px;text-align:center;font-size:16.5px;line-height:27px}
.cap-panel{left:145px;top:1508px;width:910px;height:98px;background:var(--panel)}
.cap-item{font-size:15px;color:#d6d6d6;display:flex;align-items:center;gap:10px}
.cap-item svg{flex:none}

/* contact */
.contact-title{left:0;top:2395px;width:1200px;text-align:center;font-size:31px;color:var(--orange)}
.contact-sub{left:0;top:2447px;width:1200px;text-align:center;font-family:"PT Sans",Arial,sans-serif;font-size:24px;color:var(--ink)}

/* footer */
.footer-links{left:145px;top:2736px;font-size:13px;color:var(--grey)}
.footer-links span{margin:0 9px}
.copyright{left:145px;top:2770px;font-size:13px;color:var(--grey)}
.social{top:2756px;width:16px;height:16px;border-radius:50%;background:var(--grey)}
</style>
</head>
<body>

<svg class="abs" width="1200" height="2830" style="left:0;top:0" aria-hidden="true">
  <polygon points="0,2830 0,0 1200,0 1200,2830" fill="none"/>
</svg>

<header class="site-header abs">
  <div class="brand abs"><span class="brand-mark"></span>KESTREL WORKS</div>
  <nav class="main-nav abs">
    <a class="active" href="#">HOME</a>
    <a href="#">ABOUT US</a>
    <a href="#">SOURCING</a>
    <a href="#">MACHINERY</a>
    <a href="#">CONTACT US</a>
  </nav>
</header>

<div class="hero-photo abs" role="img" aria-label="Two engineers reviewing 3D part models on computer monitors"></div>
<svg class="abs" style="left:0;top:560px" width="1200" height="95" aria-hidden="true">
  <polygon points="0,95 0,80 600,60 1200,14 1200,95" fill="#ffffff"/>
  <polygon points="600,60 1200,14 1200,91" fill="#ee5020"/>
</svg>
<div class="hero-caption abs heading">A SINGLE POINT OF CONTACT<br>FOR ALL YOUR PROCUREMENT NEEDS.</div>
<a class="btn btn-orange abs" href="#" style="left:540px;top:355px;width:118px;height:37px;line-height:37px">READ MORE</a>
<svg class="slide-arrow abs" style="left:50px" width="28" height="38" aria-hidden="true"><polyline points="24,3 6,19 24,35" fill="none" stroke="#f4d9cf" stroke-width="5"/></svg>
<svg class="slide-arrow abs" style="left:1120px" width="28" height="38" aria-hidden="true"><polyline points="4,3 22,19 4,35" fill="none" stroke="#f4d9cf" stroke-width="5"/></svg>

<section>
  <h2 class="about-title abs heading">ABOUT KESTREL WORKS</h2>
  <h3 class="about-sub abs">QUALITY POLICY</h3>
  <p class="about-copy abs">We are committed to consistently exceeding customer expectations by providing products, services and sourcing solutions of the highest standard of quality. With our streamlined processes our method is efficient, provides value and ensures on time delivery. Our success is based on continuously improving the efficiencies and effectiveness of our products, processes, and quality management systems.</p>
  <a class="btn btn-dark" href="#" style="left:145px;top:1021px;width:119px;height:49px;line-height:49px">READ MORE</a>
  <div class="about-photo abs" role="img" aria-label="Hand operating a machine control touch panel"></div>
  <svg class="abs" style="left:880px;top:732px" width="175" height="20" aria-hidden="true"><polygon points="0,0 175,0 175,20" fill="#1c1c1c"/></svg>
</section>

<svg class="abs" style="left:0;top:1150px" width="1200" height="1180" aria-hidden="true">
  <polygon points="0,82 1200,2 1200,694 0,770" fill="#1c1c1c"/>
  <polygon points="0,2 600,40 0,82" fill="#ee5020"/>
  <polygon points="0,770 1200,614 1200,1098 0,1175" fill="#ee5020"/>
  <polygon points="600,1136 1200,1098 1200,1142" fill="#1c1c1c"/>
</svg>

<section>
  <div class="service-icon abs" style="top:1283px;background:#3a3a3a" role="img" aria-label="Robotic machining arm icon"></div>
  <h2 class="service-title abs heading" style="top:1383px">MACHINING</h2>
  <p class="service-copy abs" style="top:1433px;color:var(--muted)">Whether prototype, quick-turn, short or medium run production, our In-house capabilities can help you with any machining needs you may have.</p>
  <div class="cap-panel abs">
    <div class="cap-item abs" style="left:21px;top:18px"><svg width="7" height="11"><polyline points="1,1 6,5.5 1,10" fill="none" stroke="#d6d6d6" stroke-width="1.5"/></svg>MULTIPLE AXIS EQUIPMENT</div>
    <div class="cap-item abs" style="left:21px;top:50px"><svg width="7" height="11"><polyline points="1,1 6,5.5 1,10" fill="none" stroke="#d6d6d6" stroke-width="1.5"/></svg>TOLERANCES OF +/-.0001</div>
    <div class="cap-item abs" style="left:383px;top:18px"><svg width="7" height="11"><polyline points="1,1 6,5.5 1,10" fill="none" stroke="#d6d6d6" stroke-width="1.5"/></svg>CUSTOM BUILT FIXTURES/TOOLING</div>
    <div class="cap-item abs" style="left:383px;top:50px"><svg width="7" height="11"><polyline points="1,1 6,5.5 1,10" fill="none" stroke="#d6d6d6" stroke-width="1.5"/></svg>PROTOTYPES TO PRODUCTON RUNS</div>
    <div class="cap-item abs" style="left:783px;top:18px"><svg width="7" height="11"><polyline points="1,1 6,5.5 1,10" fill="none" stroke="#d6d6d6" stroke-width="1.5"/></svg>ASSEMBLIES</div>
    <div class="cap-item abs" style="left:783px;top:50px"><svg width="7" height="11"><polyline points="1,1 6,5.5 1,10" fill="none" stroke="#d6d6d6" stroke-width="1.5"/></svg>CMM</div>
  </div>
  <a class="btn btn-dark" href="#" style="left:540px;top:1630px;width:118px;height:50px;line-height:50px">READ MORE</a>
</section>

<section>
  <div class="service-icon abs" style="top:1893px;background:#f27a52" role="img" aria-label="Connected network of people icon"></div>
  <h2 class="service-title abs heading" style="top:1992px">SOURCING</h2>
  <p class="service-copy abs" style="top:2043px;color:var(--white)">We offer a One Stop Shop solution by leveraging existing relationships and supply base knowledge to source hard to locate items, components and assemblies at the lowest cost.</p>
  <a class="btn btn-dark" href="#" style="left:540px;top:2113px;width:118px;height:52px;line-height:52px">READ MORE</a>
</section>

<section>
  <h2 class="contact-title abs heading">CONTACT US</h2>
  <p class="contact-sub abs">CONTACT US TODAY WITH YOUR MACHINING OR SOURCING NEEDS!</p>
  <a class="btn btn-orange abs heading" href="#" style="left:536px;top:2494px;width:128px;height:50px;line-height:50px;font-size:13px">GET IN TOUCH</a>
  <svg class="abs" style="left:536px;top:2537px" width="70" height="7" aria-hidden="true"><polygon points="0,0 70,7 0,7" fill="#1c1c1c"/></svg>
</section>

<svg class="abs" style="left:0;top:2625px" width="1200" height="205" aria-hidden="true">
  <polygon points="0,2 600,36 0,78" fill="#bdbdbd"/>
  <polygon points="0,78 1200,2 1200,205 0,205" fill="#1c1c1c"/>
</svg>

<footer>
  <div class="footer-links abs">Home<span>|</span>About Us<span>|</span>Sourcing<span>|</span>Machinery<span>|</span>Contact Us</div>
  <div class="copyright abs">Copyright © 2019&nbsp; Kestrel Works.&nbsp; All rights reserved.</div>
  <div class="social abs" style="left:1001px" role="img" aria-label="Social profile link"></div>
  <div class="social abs" style="left:1036px" role="img" aria-label="Social profile link"></div>
</footer>

</body>
</html>
```